Trading Company needs a business card design, letter head design and email signature

We need a double-sided business card design, letter head design and an email signature. We have a logo design.

Possible Tag Lines:
• “Connecting Worlds, Building Excellence.”
• “Trusted Trade, Steady Supply.”
• “Bridging Borders, Building Quality.”
• “Worldwide Partnerships, Superior Goods.”
• “Where Quality Meets Affordability”

Services Offered:
Procurement
Fabrication
Distribution
Logistics
Import/Export

Requirements
Must have
• Nice quality double sided Business Card design, Letterhead design needs to be A4
Nice to have
• possible ideas on tag lines

```html
<!DOCTYPE html>
<html lang="en">
<head>
<meta charset="utf-8">
<title>Corvant Stationery Set</title>
<link rel="stylesheet" href="https://fonts.googleapis.com/css2?family=Source+Sans+3:wght@400;600;700&family=Montserrat:wght@400;700;800&display=swap">
<style>
  :root {
    --red: #e8202a;
    --graphite: #58595b;
    --ink: #222222;
    --text: #444444;
    --bg: #e8e9eb;
    --paper: #ffffff;
    --black: #000000;
    --faint: #f4f4f5;
  }
  * { margin: 0; padding: 0; box-sizing: border-box; }
  html, body { width: 1200px; height: 1087px; overflow: hidden; background: var(--bg); }
  body { position: relative; font-family: "Source Sans 3", Arial, sans-serif; color: var(--text); }

  .sheet { position: absolute; background: var(--paper); box-shadow: 0 3px 8px rgba(0,0,0,.18); overflow: hidden; }
  .band { position: absolute; left: 0; right: 0; bottom: 0; display: flex; }
  .band svg { display: block; width: 100%; height: 100%; }

  /* Brand lockup */
  .brand { position: absolute; text-align: center; }
  .brand-mark { width: 30px; height: 30px; background: var(--red); margin: 0 auto 6px; }
  .brand-name { font-family: "Montserrat", sans-serif; font-weight: 800; color: var(--red); letter-spacing: 1px; line-height: 1; }
  .brand-tag { font-family: "Montserrat", sans-serif; font-weight: 700; color: var(--graphite); text-transform: uppercase; letter-spacing: .3px; margin-top: 3px; white-space: nowrap; }

  .icon { width: 9px; height: 9px; display: inline-block; vertical-align: -1px; margin-right: 4px; }

  /* Letterhead */
  .letterhead { left: 85px; top: 202px; width: 481px; height: 681px; }
  .letterhead .brand { left: 52px; top: 40px; width: 100px; }
  .letterhead .brand-mark { width: 26px; height: 26px; }
  .letterhead .brand-name { font-size: 17px; }
  .letterhead .brand-tag { font-size: 3.6px; }
  .letterhead .contact { position: absolute; left: 339px; top: 44px; font-size: 8px; line-height: 10px; color: #555; font-family: "Montserrat", sans-serif; }
  .letterhead .contact .gap { height: 5px; }
  .letterhead .contact .icon { width: 7px; height: 7px; margin-right: 3px; }
  .watermark { position: absolute; left: 160px; top: 262px; width: 190px; height: 190px; background: var(--faint); transform: rotate(45deg); }
  .letter { position: absolute; left: 48px; top: 163px; width: 390px; font-size: 7.4px; line-height: 12.8px; color: var(--text); font-family: "Montserrat", sans-serif; }
  .letter p { margin-bottom: 12.8px; }
  .signature { position: absolute; left: 48px; top: 500px; width: 58px; height: 54px; background: #eef0f4; }
  .letterhead .band { height: 9px; }

  /* Business card front (dark) */
  .card-front { left: 598px; top: 202px; width: 379px; height: 216px; background: var(--black); border-radius: 5px; }
  .card-front .brand { left: 46px; top: 70px; width: 130px; }
  .card-front .brand-name { font-size: 22px; }
  .card-front .brand-tag { font-size: 4.6px; }
  .divider { position: absolute; width: 1px; }
  .card-front .divider { left: 188px; top: 65px; height: 85px; background: var(--graphite); }
  .services { position: absolute; left: 201px; top: 64px; color: #fff; }
  .services h2 { font-family: "Montserrat", sans-serif; font-weight: 800; font-size: 10px; color: var(--red); letter-spacing: .8px; margin-bottom: 2px; }
  .services li { list-style: none; font-size: 12.5px; line-height: 15px; }
  .services li::before { content: ""; display: inline-block; width: 4px; height: 4px; border-radius: 50%; background: var(--red); margin-right: 3px; vertical-align: 3px; }

  /* Business card back (white) */
  .card-back { left: 598px; top: 439px; width: 379px; height: 216px; border-radius: 5px; }
  .card-back .brand { left: 48px; top: 66px; width: 136px; }
  .card-back .brand-name { font-size: 23px; }
  .card-back .brand-tag { font-size: 4.8px; }
  .card-back .divider { left: 194px; top: 50px; height: 115px; background: #bbb; }
  .person { position: absolute; color: var(--ink); }
  .person .name { font-weight: 700; text-transform: uppercase; color: var(--ink); }
  .person .name .first { color: var(--red); }
  .person .role, .person .addr, .person .lines { color: var(--ink); }
  .card-back .person { left: 208px; top: 52px; font-size: 11.5px; line-height: 14px; }
  .card-back .person .name { font-size: 13px; }
  .card-back .person .addr { margin-top: 10px; }
  .card-back .person .lines { margin-top: 4px; }
  .card-back .band { height: 11px; }

  /* Email signature */
  .email-sig { left: 598px; top: 701px; width: 517px; height: 183px; }
  .email-sig .brand { left: 68px; top: 31px; width: 150px; }
  .email-sig .brand-mark { width: 32px; height: 32px; }
  .email-sig .brand-name { font-size: 25px; }
  .email-sig .brand-tag { font-size: 5.2px; }
  .socials { display: flex; justify-content: center; gap: 3px; margin-top: 12px; }
  .socials span { width: 13px; height: 13px; background: var(--graphite); }
  .email-sig .divider { left: 243px; top: 26px; height: 127px; background: #bbb; }
  .email-sig .person { left: 268px; top: 30px; font-size: 13px; line-height: 16px; font-weight: 400; }
  .email-sig .person .name { font-size: 14px; }
  .email-sig .person .role { color: #444; }
  .email-sig .person .addr, .email-sig .person .lines { color: #555; }
  .email-sig .person .addr { margin-top: 9px; }
  .email-sig .person .lines { margin-top: 5px; }
  .email-sig .band { height: 10px; }
</style>
</head>
<body>

<svg width="0" height="0" style="position:absolute">
  <defs>
    <symbol id="i-phone" viewBox="0 0 24 24"><path fill="#e8202a" d="M6.6 10.8a15 15 0 0 0 6.6 6.6l2.2-2.2c.3-.3.7-.4 1-.2 1.1.4 2.3.6 3.6.6.6 0 1 .4 1 1V20c0 .6-.4 1-1 1A17 17 0 0 1 3 4c0-.6.4-1 1-1h3.5c.6 0 1 .4 1 1 0 1.3.2 2.5.6 3.6.1.3 0 .7-.2 1z"/></symbol>
    <symbol id="i-mail" viewBox="0 0 24 24"><rect x="2" y="5" width="20" height="14" fill="none" stroke="#e8202a" stroke-width="2.4"/><path d="M2 6l10 7 10-7" fill="none" stroke="#e8202a" stroke-width="2.4"/></symbol>
    <symbol id="i-globe" viewBox="0 0 24 24"><circle cx="12" cy="12" r="10" fill="none" stroke="#e8202a" stroke-width="2"/><path d="M2 12h20M12 2c3 3 3 17 0 20M12 2c-3 3-3 17 0 20" fill="none" stroke="#e8202a" stroke-width="1.8"/></symbol>
  </defs>
</svg>

<!-- Letterhead -->
<section class="sheet letterhead">
  <div class="brand">
    <div class="brand-mark"></div>
    <div class="brand-name">CORVANT</div>
    <div class="brand-tag">Trusted Trade, Steady Supply</div>
  </div>
  <div class="contact">
    <div>48 Harbor Lane Suite</div>
    <div>3 Salem, MA 01970</div>
    <div class="gap"></div>
    <div><svg class="icon"><use href="#i-phone"/></svg>(555) 310-4821</div>
    <div><svg class="icon"><use href="#i-mail"/></svg>info@corvanttrade.com</div>
    <div><svg class="icon"><use href="#i-globe"/></svg>www.corvanttrade.com</div>
  </div>
  <div class="watermark" aria-hidden="true"></div>
  <div class="letter">
    <p>Dear customer,</p>
    <p>Lorem ipsum dolor sit amet, consectetur adipisicing elit, sed do eiusmod tempor incididunt ut labore et dolore magna aliqua. Ut enim ad minim veniam, quis nostrud exercitation ullamco laboris nisi ut aliquip ex ea commodo consequat. Duis aute irure dolor in reprehenderit in voluptate velit esse cillum dolore eu fugiat nulla pariatur. Excepteur sint occaecat cupidatat non proident, sunt in culpa qui officia deserunt mollit anim id est laborum.</p>
    <p>Lorem ipsum dolor sit amet, consectetur adipisicing elit, sed do eiusmod tempor incididunt ut labore et dolore magna aliqua. Ut enim ad minim veniam, quis nostrud exercitation ullamco laboris nisi ut aliquip ex ea commodo consequat. Duis aute irure dolor in reprehenderit in voluptate velit esse cillum dolore eu fugiat nulla pariatur. Excepteur sint occaecat cupidatat non proident, sunt in culpa qui officia deserunt mollit anim id est laborum.</p>
    <p>Lorem ipsum dolor sit amet, consectetur adipisicing elit, sed do eiusmod tempor incididunt ut labore et dolore magna aliqua. Ut enim ad minim veniam, quis nostrud exercitation ullamco laboris nisi ut aliquip ex ea commodo consequat. Duis aute irure dolor in reprehenderit in voluptate velit esse cillum dolore eu fugiat nulla pariatur. Excepteur sint occaecat cupidatat non proident, sunt in culpa qui officia deserunt mollit anim id est laborum.</p>
    <p>Lorem ipsum dolor sit amet, consectetur adipisicing elit, sed do eiusmod tempor incididunt ut labore et dolore magna aliqua. Ut enim ad minim veniam, quis nostrud exercitation ullamco laboris nisi ut aliquip ex ea commodo consequat. Duis aute irure dolor in reprehenderit.</p>
    <p>Yours Sincerely,</p>
  </div>
  <div class="signature" role="img" aria-label="Handwritten signature"></div>
  <div class="band">
    <svg viewBox="0 0 481 9" preserveAspectRatio="none"><polygon points="0,0 370,0 364,9 0,9" fill="#e8202a"/><polygon points="370,0 481,0 481,9 364,9" fill="#58595b"/></svg>
  </div>
</section>

<!-- Business card front -->
<section class="sheet card-front">
  <div class="brand">
    <div class="brand-mark"></div>
    <div class="brand-name">CORVANT</div>
    <div class="brand-tag">Trusted Trade, Steady Supply</div>
  </div>
  <div class="divider"></div>
  <div class="services">
    <h2>SERVICES OFFERED:</h2>
    <ul>
      <li>Procurement</li>
      <li>Fabrication</li>
      <li>Distribution</li>
      <li>Logistics</li>
      <li>Import/Export</li>
    </ul>
  </div>
</section>

<!-- Business card back -->
<section class="sheet card-back">
  <div class="brand">
    <div class="brand-mark"></div>
    <div class="brand-name">CORVANT</div>
    <div class="brand-tag">Trusted Trade, Steady Supply</div>
  </div>
  <div class="divider"></div>
  <div class="person">
    <div class="name"><span class="first">Dana</span> Whitfield</div>
    <div class="role">Founder &amp; CEO</div>
    <div class="addr">48 Harbor Lane Suite<br>3 Salem, MA 01970</div>
    <div class="lines">
      <div><svg class="icon"><use href="#i-phone"/></svg>(555) 310-4821</div>
      <div><svg class="icon"><use href="#i-mail"/></svg>info@corvanttrade.com</div>
      <div><svg class="icon"><use href="#i-globe"/></svg>www.corvanttrade.com</div>
    </div>
  </div>
  <div class="band">
    <svg viewBox="0 0 379 11" preserveAspectRatio="none"><polygon points="0,0 200,0 194,11 0,11" fill="#e8202a"/><polygon points="200,0 379,0 379,11 194,11" fill="#58595b"/></svg>
  </div>
</section>

<!-- Email signature -->
<section class="sheet email-sig">
  <div class="brand">
    <div class="brand-mark"></div>
    <div class="brand-name">CORVANT</div>
    <div class="brand-tag">Trusted Trade, Steady Supply</div>
    <div class="socials" aria-label="Social profiles"><span></span><span></span><span></span><span></span></div>
  </div>
  <div class="divider"></div>
  <div class="person">
    <div class="name"><span class="first">Leon R.</span> Marsh, Esq.</div>
    <div class="role">Managing Director</div>
    <div class="addr">72 Maple Ridge Road,<br>Markham, ON L3R 5K1</div>
    <div class="lines">
      <div><svg class="icon"><use href="#i-phone"/></svg>(555) 720-3390</div>
      <div><svg class="icon"><use href="#i-mail"/></svg>leon@corvanttrade.com</div>
      <div><svg class="icon"><use href="#i-globe"/></svg>www.corvanttrade.com</div>
    </div>
  </div>
  <div class="band">
    <svg viewBox="0 0 517 10" preserveAspectRatio="none"><polygon points="0,0 249,0 244,10 0,10" fill="#e8202a"/><polygon points="249,0 517,0 517,10 244,10" fill="#58595b"/></svg>
  </div>
</section>

</body>
</html>
```